Web Site Redesign

We operate a data centre facility specialing in colocation and Fibre optic connectivity (i.e. point to point fibre services and internet over fibre).

We have an existing site located at www.norvalex.example however this is very very tired and requires a redesign. We are looking for a fresh new design that will be appealing to potential customers.

The Company name is Norva eX and the primary corporate colour is bright red with secondary colours of white, grey and black. Specific bright red can be seen in attached company logo.

Website needs to be modern, clean and professional representing our premium colocation and fibre provider branding.

Our company slogan is : safe. secure. reliable

We will provide feedback regardless of the quality of the design to ensure a better outcome for all parties.

Please feel free to contact us if you have any questions.

# The designer can use placeholder images or feel free to use any/all or none of the attached images
# The designer can use sample filler text

Target Market(s)

Technical IT Professionals as well C level executives (i.e. CEO's, CIO).

Industry/Entity Type

Internet

Requirements
Must have
• clean design
Nice to have
• A sidebar with two sections. 1 for current promo and 1 for "Let us call you back/contact you"
Should not have
• Clutter

```html
<!DOCTYPE html>
<html lang="en">
<head>
<meta charset="utf-8">
<title>Norva eX — safe. secure. reliable</title>
<link href="https://fonts.googleapis.com/css2?family=Michroma&family=PT+Sans:wght@400;700&display=swap" rel="stylesheet">
<style>
:root{
  --red:#e8262b;
  --red-dark:#c91c21;
  --ink:#222222;
  --grey:#444444;
  --grey-mid:#777777;
  --grey-light:#bdbdbd;
  --white:#ffffff;
  --band:#3a3a3a;
}
*{box-sizing:border-box;margin:0;padding:0}
html,body{width:1056px;height:1200px;overflow:hidden;background:var(--white)}
body{font-family:"PT Sans",Tahoma,sans-serif;color:var(--ink);font-size:13.5px}
.canvas{position:relative;width:1056px;height:1200px;overflow:hidden}
.abs{position:absolute}
a{color:inherit;text-decoration:none}

.top-rule{left:50px;top:16px;width:500px;height:5px;background:linear-gradient(to right,var(--red) 0 85%,var(--band) 85% 100%)}
.slogan{left:556px;top:6px;font-family:"Michroma",sans-serif;font-size:29px;letter-spacing:1px;color:var(--grey);white-space:nowrap}
.slogan .hl{color:var(--red)}
.tagline{left:551px;top:47px;font-size:14.5px;letter-spacing:.6px;color:var(--grey);white-space:nowrap}

.brand{left:56px;top:148px;display:flex;align-items:center;gap:10px}
.brand-mark{width:22px;height:22px;background:var(--red)}
.brand-name{font-size:30px;color:var(--ink);font-weight:400}

.util-nav{right:48px;top:164px;font-size:13.5px;color:var(--ink)}
.util-nav span{margin:0 12px;color:var(--ink)}

.main-nav{left:50px;top:195px;width:958px;height:83px;background:linear-gradient(to bottom,#ef3a3e,var(--red-dark));border-bottom:6px solid #111;display:flex}
.main-nav a{flex:1;display:flex;align-items:center;justify-content:center;color:var(--white);font-size:13.5px;border-left:1px solid rgba(0,0,0,.25);padding-top:4px}
.main-nav a:first-child{border-left:none;font-weight:700}

.hero{left:50px;top:285px;width:958px;height:303px;background:linear-gradient(100deg,#b9b6b0 0%,#8f8a84 30%,#3c3c3e 55%,#1b1b1d 75%,#6d6a66 100%);border-bottom:5px solid var(--band)}
.hero-copy{left:606px;top:40px;color:var(--white);line-height:1}
.hero-copy .l1{font-size:31px;font-weight:400}
.hero-copy .l2{font-size:29px;font-weight:700;margin:5px 0 0 38px}
.hero-copy .l3{font-size:24px;margin:4px 0 0 26px}
.hero-stop{right:0;bottom:3px;width:160px;height:38px;background:var(--red);color:var(--white);font-size:13.5px;display:flex;align-items:center;padding-left:45px;border-left:22px solid var(--band)}

.section-title{font-family:"Michroma",sans-serif;font-size:24px;color:var(--ink);white-space:nowrap;letter-spacing:.5px}
.section-title .hl{color:var(--red)}

.news-title{left:63px;top:638px}
.news-item{left:88px;width:300px}
.news-date{display:inline-block;height:28px;line-height:28px;width:117px;background:var(--red);color:var(--white);font-size:13.5px;padding-left:26px;border-left:11px solid var(--band)}
.news-text{margin-top:14px;line-height:17.5px;font-size:13.5px}
.news-links{left:87px;top:1031px;color:var(--red);font-size:13.5px}
.news-links span{color:var(--ink);margin:0 6px}

.divider{left:405px;top:688px;height:318px;border-left:1px dotted var(--grey-mid)}

.welcome-title{left:437px;top:638px}
.welcome-body{left:435px;top:706px;width:560px;line-height:17.5px;font-size:13.5px}
.welcome-body .lead{color:var(--red)}
.welcome-body p+p{margin-top:17.5px}
.welcome-more{left:951px;top:879px;color:var(--red);font-size:13.5px}

.services-title{left:432px;top:928px}
.services{top:967px;list-style:none;font-size:13.5px;line-height:22.5px}
.services li{display:flex;align-items:center;gap:10px}
.services svg{flex:none}
.services.col-a{left:432px}
.services.col-b{left:725px}

.footer-rule{left:50px;top:1094px;width:958px;height:4px;background:var(--band)}
.partners-note{left:50px;top:1112px;font-size:13.5px}
.partners{left:44px;top:1140px;display:flex;align-items:center;gap:26px;height:42px}
.partner{font-size:15px;color:var(--grey)}
.partner.p1{color:var(--red)}
.partner.p2{color:var(--red)}
.partner.p3{color:#2aa8d8}
.legal{right:50px;top:1143px;font-size:13.5px}
.legal .red{color:var(--red)}
</style>
</head>
<body>
<div class="canvas">

  <div class="abs top-rule"></div>
  <div class="abs slogan">safe. <span class="hl">secure.</span> reliable</div>
  <div class="abs tagline">CALL US TODAY TO SEE HOW WE CAN HELP MEET YOUR NEEDS.</div>

  <a class="abs brand" href="#"><span class="brand-mark"></span><span class="brand-name">Norva eX</span></a>

  <nav class="abs util-nav"><a href="#">home</a><span>|</span><a href="#">sitemap</a><span>|</span><a href="#">FAQs</a></nav>

  <nav class="abs main-nav">
    <a href="#">Home</a>
    <a href="#">About us</a>
    <a href="#">Facilities</a>
    <a href="#">Business Continuity</a>
    <a href="#">Services</a>
    <a href="#">WebMail</a>
    <a href="#">Contact us</a>
  </nav>

  <section class="abs hero" role="img" aria-label="Photo of a woman working on a laptop">
    <div class="abs hero-copy">
      <div class="l1">Perth's Safe,</div>
      <div class="l2">Secure &amp; Reliable</div>
      <div class="l3">Data Centre</div>
    </div>
    <a class="abs hero-stop" href="#">stop animation</a>
  </section>

  <h2 class="abs section-title news-title">latest<span class="hl">news</span></h2>

  <article class="abs news-item" style="top:710px">
    <span class="news-date">12.07.2010</span>
    <p class="news-text">Lorem ipsum dolor sit amet, consectetuer adipi esent vestibulum molestie lacus. Aenean</p>
  </article>
  <article class="abs news-item" style="top:810px">
    <span class="news-date">12.07.2010</span>
    <p class="news-text">Lorem ipsum dolor sit amet, consectetuer adipi esent vestibulum molestie lacus. Aenean</p>
  </article>
  <article class="abs news-item" style="top:910px">
    <span class="news-date">12.07.2010</span>
    <p class="news-text">Lorem ipsum dolor sit amet, consectetuer adipiscing elitra esent vestibulum molestie</p>
  </article>

  <div class="abs news-links"><a href="#">MORE NEWS</a><span>|</span><a href="#">NEWSLETTER</a></div>

  <div class="abs divider"></div>

  <h2 class="abs section-title welcome-title">Welcome <span class="hl">to Norva eX</span></h2>
  <div class="abs welcome-body">
    <p><span class="lead">A world class data centre in the safest place on Earth.</span><br>With a centrally located data centre in the heart of the Perth CBD Norva eX is excellently positioned to assist with your critical IT requirements.</p>
    <p>The CBD facility features overlapping power grids, redundant power supplies and comprehensively maintained infrastructure, providing excellent levels of protection for your critical IT equipment. The State's newest and most technologically advanced data centre is also now open in Belmont, a convenient 5.5 km's from the CBD providing a perfect location for either production sites, or DR infrastructure.</p>
  </div>
  <a class="abs welcome-more" href="#">MORE</a>

  <h2 class="abs section-title services-title">featured<span class="hl">services</span></h2>
  <ul class="abs services col-a">
    <li><svg width="12" height="8" viewBox="0 0 12 8"><path d="M0 4h8M6 1l3 3-3 3" stroke="#999" fill="none" stroke-dasharray="1.5 1"/></svg>Co-location</li>
    <li><svg width="12" height="8" viewBox="0 0 12 8"><path d="M0 4h8M6 1l3 3-3 3" stroke="#999" fill="none" stroke-dasharray="1.5 1"/></svg>Fibre connectivity</li>
    <li><svg width="12" height="8" viewBox="0 0 12 8"><path d="M0 4h8M6 1l3 3-3 3" stroke="#999" fill="none" stroke-dasharray="1.5 1"/></svg>Web Hosting</li>
    <li><svg width="12" height="8" viewBox="0 0 12 8"><path d="M0 4h8M6 1l3 3-3 3" stroke="#999" fill="none" stroke-dasharray="1.5 1"/></svg>Remote offsite backups</li>
  </ul>
  <ul class="abs services col-b">
    <li><svg width="12" height="8" viewBox="0 0 12 8"><path d="M0 4h8M6 1l3 3-3 3" stroke="#e8262b" fill="none" stroke-dasharray="1.5 1"/></svg>Managed and hosted software solutions</li>
    <li><svg width="12" height="8" viewBox="0 0 12 8"><path d="M0 4h8M6 1l3 3-3 3" stroke="#e8262b" fill="none" stroke-dasharray="1.5 1"/></svg>Internet Connectivity via Fibre</li>
    <li><svg width="12" height="8" viewBox="0 0 12 8"><path d="M0 4h8M6 1l3 3-3 3" stroke="#e8262b" fill="none" stroke-dasharray="1.5 1"/></svg>Business grade DSL (Both ADSL and SHDSL)</li>
    <li><svg width="12" height="8" viewBox="0 0 12 8"><path d="M0 4h8M6 1l3 3-3 3" stroke="#e8262b" fill="none" stroke-dasharray="1.5 1"/></svg>Point to Point Licensed Microwave links</li>
  </ul>

  <div class="abs footer-rule"></div>
  <p class="abs partners-note">Norva eX partners with Australia's leading providers of IT solutions and infrastructure.</p>
  <div class="abs partners">
    <span class="partner p1">Corvane Telecom</span>
    <span class="partner p2">Brightlink</span>
    <span class="partner p3">Tellura</span>
    <span class="partner p4">Rowan Consultants</span>
  </div>
  <p class="abs legal">Norva eX © 2010 | <a class="red" href="#">Privacy Policy</a> | <a href="#">Terms Of Use</a></p>

</div>
</body>
</html>
```